Can You Break Boring? - Design a Dazzling Conference Program!

The 35th Annual PLMR Conference and Trade Show is the Top-Notch event for Veterinary Technicians in Canada. With a reputation like that, the program has to knock the delegates socks off!
Are you up to the challenge?
The PLMR will provide you with the following:
-venue information (hours, floorplan etc.)
-conference logo and theme
-speaker bios and lecture abstracts (58 speakers, over 108 sessions)
-4 day agenda
-images that have been used in marketing to date
-color schemes that are preferred
We are looking for someone to take the material and create a program that is colorful, engaging and unique.
A copy of the registration brochure is attached. The winning submission will strongly resemble this document.
Updates

Project Deadline Extended
Reason: The submissions are getting closer to what we are looking for so we wish to extend the deadline to provide designers more time to submit more ideas.

Project Deadline Extended
Reason: I am looking for more concepts on the interior layout now. Please submit your ideas for: - exhibitor info pages - speaker info/lecture info pages - venue info - floorplan and agenda pages.

Target Market(s)

approx. 1200 Veterinary Technician delegates attending the conference

Industry/Entity Type

Marketing

Requirements
Must have
• - conference logo and theme (provided)
- PLMR logo (provided)
- venue floor plans
- conference schedule
- speaker bios and session abstracts
STRONG relation to the registration brochure.

```html
<!DOCTYPE html>
<html lang="en">
<head>
<meta charset="utf-8">
<title>35th Annual Conference – PLMR</title>
<link href="https://fonts.googleapis.com/css2?family=Arimo:ital,wght@0,400;0,700;1,400&family=Bebas+Neue&family=Orbitron:wght@500&family=Roboto+Condensed:wght@400&display=swap" rel="stylesheet">
<style>
  :root {
    --purple: #5f2f6b;
    --purple-text: #6d2c72;
    --sea-dark: #1a86b0;
    --sea-light: #3bb4d6;
    --mist: #d3e5ef;
    --sky-text: #2b9cc6;
    --ink: #111111;
    --grey: #7d7d7d;
    --stone: #9ba5a0;
    --white: #ffffff;
    --ember: #d9532b;
  }
  * { margin: 0; padding: 0; box-sizing: border-box; }
  html, body { width: 1200px; height: 1200px; overflow: hidden; background: var(--white); }
  .poster { position: relative; width: 1200px; height: 1200px; font-family: "Arimo", Arial, sans-serif; color: var(--ink); }
  .backdrop { position: absolute; inset: 0; }
  .txt { position: absolute; white-space: nowrap; line-height: 1; }
  .tagline { color: var(--white); font-size: 31px; letter-spacing: 2px; }
  .section-title { color: var(--sky-text); font-size: 31px; letter-spacing: 2.5px; font-weight: 400; }
  .register-line { font-size: 22px; letter-spacing: 1px; }
  .register-url { font-size: 25px; font-weight: 700; letter-spacing: 3px; }
  .register-phone { font-family: "Roboto Condensed", "Arial Narrow", sans-serif; font-size: 22px; }
  .track-list { position: absolute; list-style: none; font-size: 18px; }
  .track-list li { height: 25.5px; line-height: 25.5px; white-space: nowrap; }
  .track-list .sub { font-style: italic; color: var(--grey); font-size: 16px; padding-left: 28px; }
  .track-list .sub .item { margin-right: 26px; }
  .track-list .sub .big { font-size: 20px; }
  .org-mark { position: absolute; left: 200px; top: 852px; display: flex; align-items: center; gap: 18px; }
  .org-mark .dot { width: 74px; height: 74px; border-radius: 50%; background: var(--sky-text); opacity: .55; }
  .org-mark .name { font-size: 32px; font-weight: 700; color: var(--grey); letter-spacing: 2px; }
  .org-word { left: 164px; top: 1036px; font-size: 44px; color: var(--stone); letter-spacing: 8px; font-weight: 700; }
  .venue { left: 25px; width: 1200px; top: 1166px; text-align: center; font-family: "Roboto Condensed", "Arial Narrow", sans-serif; font-size: 24px; letter-spacing: .5px; }
  .venue-mark { position: absolute; left: 935px; top: 1098px; display: flex; align-items: flex-start; gap: 8px; }
  .venue-mark .square { width: 26px; height: 26px; background: var(--ember); }
  .venue-mark .name { font-family: "Roboto Condensed", "Arial Narrow", sans-serif; font-size: 17px; line-height: 1.05; color: var(--ink); }
</style>
</head>
<body>
<main class="poster">
  <svg class="backdrop" width="1200" height="1200" viewBox="0 0 1200 1200">
    <defs>
      <linearGradient id="sea" x1="0" y1="0" x2="1" y2="1">
        <stop offset="0" stop-color="#1a86b0"/>
        <stop offset="0.55" stop-color="#3bb4d6"/>
        <stop offset="1" stop-color="#1a86b0"/>
      </linearGradient>
      <linearGradient id="emblem-fill" x1="0" y1="0" x2="1" y2="0">
        <stop offset="0" stop-color="#3fa06a"/>
        <stop offset="0.5" stop-color="#2f6fb0"/>
        <stop offset="1" stop-color="#8d2f85"/>
      </linearGradient>
    </defs>
    <rect class="header-band" x="134" y="0" width="932" height="126" fill="#5f2f6b"/>
    <rect class="sea-panel" x="134" y="126" width="932" height="426" fill="url(#sea)"/>
    <path class="sea-swoosh" d="M134 150 C 450 140, 800 200, 1066 330 L1066 380 C 800 260, 450 190, 134 200 Z" fill="#ffffff" opacity=".08"/>
    <path class="sea-edge" d="M134 552 L134 560 L1066 560 L1066 512 C 900 535, 760 548, 660 552 Z" fill="#ffffff"/>
    <path class="mist-panel" d="M690 552 C 560 680, 470 880, 455 1200 L 760 1200 C 880 1150, 990 1115, 1066 1085 L1066 552 Z" fill="#d3e5ef"/>
    <rect x="132" y="0" width="3" height="1200" fill="#5f2f6b"/>
    <rect x="1065" y="0" width="3" height="1200" fill="#5f2f6b"/>
    <rect class="emblem" x="174" y="318" width="360" height="200" rx="30" fill="url(#emblem-fill)" opacity=".75" role="img" aria-label="Conference emblem: infinity loop with farm, companion and exotic animals"/>
    <text x="150" y="112" font-family="Bebas Neue, sans-serif" font-size="130" fill="#ffffff" textLength="150" lengthAdjust="spacingAndGlyphs">35</text>
    <text x="306" y="60" font-family="Bebas Neue, sans-serif" font-size="66" fill="#ffffff" textLength="80" lengthAdjust="spacingAndGlyphs">TH</text>
    <text x="410" y="112" font-family="Bebas Neue, sans-serif" font-size="120" fill="#ffffff" textLength="640" lengthAdjust="spacingAndGlyphs">ANNUAL CONFERENCE</text>
    <text x="846" y="172" font-family="Arimo, sans-serif" font-size="44" fill="#6d2c72" textLength="206" lengthAdjust="spacingAndGlyphs">ONTARIO</text>
    <text x="182" y="180" font-family="Orbitron, sans-serif" font-size="32" fill="#ffffff" textLength="516" lengthAdjust="spacing">FEBRUARY 21-23 2013</text>
    <text x="422" y="252" font-family="Orbitron, sans-serif" font-size="32" fill="#ffffff" textLength="544" lengthAdjust="spacing">CONFERENCE &amp; TRADE</text>
  </svg>

  <p class="txt tagline" style="left:574px; top:344px;">Respecting our Past</p>
  <p class="txt tagline" style="left:646px; top:466px;">Embracing our Feature</p>

  <h2 class="txt section-title" style="left:170px; top:572px;">Register Today</h2>
  <p class="txt register-line" style="left:168px; top:640px;">Safe, Secure, On Line at</p>
  <p class="txt register-url" style="left:170px; top:688px;">www.plmr-events.org</p>
  <p class="txt register-phone" style="left:161px; top:752px;">More info: call 1-800-555-0142</p>

  <div class="org-mark"><span class="dot"></span><span class="name">PLMR</span></div>
  <p class="txt org-word">PLMR</p>

  <h2 class="txt section-title" style="left:677px; top:572px;">Conference Tracks</h2>
  <ul class="track-list" style="left:680px; top:619px;">
    <li>Personal Grow and Comunication</li>
    <li>Practice Managment and Social Media</li>
    <li>Nutrition</li>
    <li>Special interest</li>
    <li class="sub"><span class="item">One health</span><span class="item">Personal finance</span></li>
    <li>Pain and rehabilitation</li>
  </ul>
  <ul class="track-list" style="left:634px; top:795px;">
    <li>Equine medicine and Equine anesthesia</li>
    <li>Large animal medicine</li>
    <li>Small animal medicine</li>
    <li class="sub"><span class="item big">-Surgery</span><span class="item"><span class="big">-Onco</span>logy</span><span class="item">-Dentistry</span></li>
    <li>Lab animals and research</li>
    <li>Special topics</li>
  </ul>
  <ul class="track-list" style="left:506px; top:977px;">
    <li>Emergency and critical care</li>
    <li>Anesthesia</li>
    <li>Exotics</li>
    <li>Diagnostic imagin</li>
    <li>Behavior</li>
  </ul>

  <p class="txt venue">RIVERSIDE CONVENTION CENTRE &amp; GRANDVIEW HOTEL</p>
  <div class="venue-mark"><span class="square"></span><span class="name">RIVERSIDE<br>CONVENTION<br>CENTRE</span></div>
</main>
</body>
</html>
```